Redesign of page from emergency manual

Please redesign this PDF to look better. Please don't include any stock photos. It must be legible. Making some words bold is probably a good idea.

Here are some things I like :

https://tarrowbooks.com.au/collections/frontpage/products/the-plk-v2-ebook

https://img-cd.vostramediafiles.com/qa-ejkwPLOTYY_SuCKbZNu411Qwgjv8YssPxEdzXN93hDkSRjLXK8WmfgbmrJW4ZZ3yUPK=w1052-h592-rw

```html
<!DOCTYPE html>
<html lang="en">
<head>
<meta charset="utf-8">
<title>Hypertension, Acute</title>
<link rel="stylesheet" href="https://fonts.googleapis.com/css2?family=Montserrat:wght@400;500;700&display=swap">
<style>
:root{
  --backdrop:#d6ebf2;
  --card:#ffffff;
  --sky:#8fd4ea;
  --sky-pale:#dff2f9;
  --ink:#111111;
  --text:#222222;
  --black:#0a0a0a;
  --teal-text:#86d6ea;
}
*{box-sizing:border-box;margin:0;padding:0}
html,body{width:1200px;height:1200px;overflow:hidden}
body{background:var(--backdrop);font-family:"Montserrat",Arial,sans-serif;color:var(--text);position:relative}
.card{position:absolute;left:50px;top:212px;width:1100px;height:775px;background:var(--card);overflow:hidden}
.abs{position:absolute}
.intro-panel{left:0;top:0}
.title{left:40px;top:28px;font-size:24px;font-weight:700;color:var(--ink)}
.intro{left:40px;top:80px;width:545px;font-size:15px;line-height:1.32}
.intro p{margin-bottom:14px}
.intro p.tight{margin-bottom:0}
.summary{left:598px;top:10px;width:502px;height:59px;background:var(--black);color:var(--teal-text);font-size:15px;line-height:1.3;text-align:center;display:flex;align-items:center;justify-content:center}
.side-band{left:1031px;top:69px;width:69px}
.side-title{left:1066px;top:225px;transform-origin:0 0;transform:translate(14px,0) rotate(90deg);white-space:nowrap;font-size:27px;font-weight:700;color:var(--ink)}
.bp-table{left:625px;top:88px;width:378px;border-collapse:collapse;font-size:15px}
.bp-table th,.bp-table td{border:1.5px solid var(--ink);height:31px;padding:0 10px;text-align:left;font-weight:400}
.bp-table caption{background:var(--sky);border:1.5px solid var(--ink);border-bottom:none;font-weight:700;font-size:16px;color:var(--ink);padding:3px 0}
.caution{left:40px;top:270px;width:1000px;font-size:15px;line-height:1.3}
.caution strong{color:var(--ink)}
.drug-table{left:40px;top:346px;width:991px;border-collapse:collapse;font-size:15px}
.drug-table th{height:44px;font-size:21px;font-weight:700;color:var(--ink);border:1.5px solid var(--ink)}
.drug-table td{border:1.5px solid var(--ink);padding:6px 28px;line-height:1.3}
.drug-table td.action{width:312px;background:var(--sky-pale)}
.drug-table tr.plain td.action{background:var(--card)}
.diff-tab{left:0;top:625px}
.diff-label{left:40px;top:638px;font-size:14px;font-weight:700;color:var(--ink)}
.diff-col{top:685px;font-size:15px;line-height:1.3}
.diff-col.one{left:40px}
.diff-col.two{left:400px}
.diff-col.three{left:850px}
</style>
</head>
<body>
<main class="card">
  <svg class="abs intro-panel" width="600" height="245" viewBox="0 0 600 245" aria-hidden="true">
    <path d="M0,69 L319,69 L375,12 L600,12 L600,212 Q600,244 568,244 L0,244 Z" fill="var(--sky)"/>
  </svg>
  <h1 class="abs title">Hypertension, Acute</h1>
  <div class="abs intro">
    <p>•In pediatrics, hypertension is almost always treated by addressing likely causes such as light anesthesia or measurement error:</p>
    <p>• Ensure correct BP cuff size: cuff bladder width - 40% of limb circumference</p>
    <p class="tight">• Ensure arterial line transducer is at level of heart</p>
    <p class="tight">- Consider placing arterial line if not already present</p>
  </div>

  <div class="abs summary">Sustained high blood pressure refractory<br>to treating reversible causes</div>

  <svg class="abs side-band" width="69" height="706" viewBox="0 0 69 706" aria-hidden="true">
    <rect x="0" y="0" width="69" height="706" fill="var(--sky)"/>
    <polygon points="0,591 69,572 69,706 0,706" fill="var(--black)"/>
    <polygon points="0,584 69,565 69,570 0,589" fill="#ffffff"/>
  </svg>
  <div class="abs side-title">Hypertension, Acute</div>

  <table class="abs bp-table">
    <caption>Hypertensive Blood Pressure Range*</caption>
    <tr><th>Age (yr)</th><th>Systolic</th><th>Diastolic</th></tr>
    <tr><td>newborn</td><td>&gt;97</td><td>&gt;70</td></tr>
    <tr><td>1-3</td><td>&gt;105</td><td>&gt;61</td></tr>
    <tr><td>4-12</td><td>&gt;113</td><td>&gt;86</td></tr>
  </table>

  <p class="abs caution"><strong>* CAUTION:</strong> Anti-hypertensive drugs are almost never needed for routine pediatric cases. These medications are used almost exclusively for specialized cardiac, neurosurgical, or endocrine (pheochromocytoma) cases. Consult an expert before use. Rule-out increased ICP.</p>

  <table class="abs drug-table">
    <tr><th>Action</th><th>Drug (IV Dosing)</th></tr>
    <tr><td class="action">Direct smooth muscle relaxation</td>
      <td>§ Sodium nitroprusside 0.5-10 MICROgrams/kg/min<br>§ HydrALAZINE 0.1-0.2 mg/kg (adult dose 5-10 mg)</td></tr>
    <tr class="plain"><td class="action">β-Adrenergic blockade</td>
      <td>Esmolol 100-500 MICROgrams/kg over 5 min, then<br>25-300 MICROgrams/kg/min<br>§ Labetalol (also a effect) 0.2-1 mg/kg q 10 min; 0.4-3 mg/kg/hour (infusion)</td></tr>
    <tr><td class="action">Calcium channel blockade</td>
      <td>§ niCARdapine 0.5-5 MICROgrams/kg/min<br>§ Clevidipine 0.5-3.5 MICROgrams/kg/min</td></tr>
    <tr class="plain"><td class="action">D1-dopamine agonist</td>
      <td>§ Fenoldopam 0.2-0.8 MICROgrams/kg/min</td></tr>
  </table>

  <svg class="abs diff-tab" width="345" height="44" viewBox="0 0 345 44" aria-hidden="true">
    <path d="M0,0 L345,0 L315,44 L0,44 Z" fill="var(--sky)"/>
  </svg>
  <div class="abs diff-label">Consider Differential (Partial):</div>

  <div class="abs diff-col one">• Light anesthesia (consider vaporizer<br>or infusion pump empty or malfunctioning)<br>• Hypercarbia</div>
  <div class="abs diff-col two">Hypoxemia<br>• Arterial line transducer too low or BP cuff too small<br>• Withdrawal (EtOH or opioid)</div>
  <div class="abs diff-col three">• Thyroid Storm<br>• Pheochromocytoma<br>• Drug Error</div>
</main>
</body>
</html>
```